Business Cards, Letterheads, Envelopes

A company's new identity to be reflected on its stationery items

Target Market(s)

Large Corporate Companies & Enterprises

Font styles to use
Sans Serif

Colors
0555a3
3176b5
85abd2
85cae6
33a6d7
0293ce

```html
<!DOCTYPE html>
<html lang="en">
<head>
<meta charset="utf-8">
<title>Nodeway Summit Stationery</title>
<link href="https://fonts.googleapis.com/css2?family=Montserrat:wght@400;500;600;700&display=swap" rel="stylesheet">
<style>
:root{
  --navy:#0555a3;
  --blue:#3176b5;
  --sky:#85abd2;
  --aqua:#85cae6;
  --cyan:#33a6d7;
  --brand:#0293ce;
  --card-blue:#3a8bd0;
  --paper:#ffffff;
  --stage:#e8e9eb;
  --ink:#2d3b4a;
  --muted:#6b7785;
  --grey-band:#9b9ea3;
}
*{margin:0;padding:0;box-sizing:border-box}
html,body{width:1200px;height:960px;overflow:hidden}
body{background:var(--stage);font-family:"Montserrat",sans-serif;color:var(--ink);position:relative}
.sheet{position:absolute;background:var(--paper);overflow:hidden}
.wordmark{display:flex;align-items:center;gap:8px}
.wordmark .dot{width:26px;height:26px;border-radius:50%;border:2px solid var(--blue);flex:none}
.wordmark .name{font-weight:600;color:var(--blue);text-transform:uppercase;letter-spacing:.06em;line-height:1.15}
.wordmark .tagline{font-size:5px;letter-spacing:.3em;color:var(--muted);text-transform:uppercase;margin-top:3px}

/* Letterhead */
.letterhead{left:70px;top:157px;width:469px;height:656px}
.letterhead .wordmark{position:absolute;left:22px;top:14px}
.letterhead .name{font-size:10px}
.letterhead .rule-top{position:absolute;left:190px;right:0;top:30px;height:2px;background:var(--blue)}
.letterhead .rule-under{position:absolute;left:0;top:52px;width:206px;height:4px;background:var(--blue)}
.letterhead .network{position:absolute;left:195px;top:180px;right:0;bottom:10px;
  background:radial-gradient(ellipse at 70% 55%,#c3dbef 0%,#d7e7f5 45%,rgba(255,255,255,0) 75%)}
.letterhead .contact{position:absolute;right:28px;bottom:16px;display:flex;gap:16px;font-size:8px;color:var(--blue)}
.contact span{display:flex;align-items:center;gap:4px}
.contact svg{width:9px;height:9px}
.letterhead .band{position:absolute;left:0;right:0;bottom:0;height:8px;background:var(--blue)}

/* Business cards */
.card{width:216px;height:127px;left:680px}
.card-front{top:182px;background:var(--card-blue)}
.card-front .network{position:absolute;left:0;top:0;width:58px;height:127px;
  background:linear-gradient(90deg,rgba(255,255,255,.55),rgba(255,255,255,.15))}
.card-front .name-block{position:absolute;left:72px;top:50px;color:#fff}
.card-front .name{font-size:10px;font-weight:600;letter-spacing:.08em;line-height:1.2;text-transform:uppercase}
.card-front .tagline{font-size:5px;letter-spacing:.35em;margin-top:4px;text-transform:uppercase}
.card-front .web-band{position:absolute;left:72px;right:0;top:98px;height:10px;background:#fff;
  font-size:6px;font-weight:700;letter-spacing:.2em;color:var(--card-blue);display:flex;align-items:center;justify-content:flex-end;padding-right:32px}
.card-back{top:333px}
.card-back .wordmark{position:absolute;left:62px;top:16px}
.card-back .dot{width:18px;height:18px}
.card-back .name{font-size:7px}
.card-back .tagline{font-size:3.5px}
.card-back .divider{position:absolute;left:40px;right:40px;top:45px;height:1px;background:#c9d2dc}
.card-back .person{position:absolute;left:0;right:0;top:50px;text-align:center;font-size:7px}
.person .full{color:var(--blue);font-weight:600;font-size:8px}
.person .role{font-weight:600;color:var(--ink)}
.person .bar{margin:0 6px;color:var(--ink)}
.card-back .address{position:absolute;left:0;right:0;top:78px;text-align:center;font-size:5px;color:var(--muted)}
.card-back .lines{position:absolute;left:48px;right:40px;top:90px;display:flex;justify-content:space-between;font-size:5px;color:var(--muted)}
.card-back svg{width:6px;height:6px;vertical-align:-1px;margin-right:2px}
.card-back .grey-band{position:absolute;left:0;right:0;bottom:8px;height:6px;background:var(--grey-band)}

/* Envelope */
.envelope{left:639px;top:533px;width:459px;height:238px}
.envelope .top-rule{position:absolute;left:0;right:0;top:0;height:4px;background:var(--blue)}
.envelope .wordmark{position:absolute;left:22px;top:36px}
.envelope .name{font-size:10px}
.envelope .network{position:absolute;left:255px;top:4px;right:0;height:190px;
  background:radial-gradient(ellipse at 60% 35%,#bccfea 0%,#d5e1f3 45%,rgba(255,255,255,0) 75%)}
.envelope .window{position:absolute;left:215px;top:116px;width:200px;height:88px;border-radius:8px;
  background:linear-gradient(180deg,#f3f3f4,#e4e5e7);box-shadow:inset 0 0 6px rgba(0,0,0,.12)}
.envelope .return{position:absolute;left:10px;top:175px;font-size:5px;color:var(--muted)}
.return div{display:flex;align-items:center;gap:5px;margin-bottom:3px}
.return .sq{width:7px;height:7px;background:var(--blue);flex:none}
.return .gap{margin-top:8px}
.envelope .band{position:absolute;left:0;right:0;bottom:0;height:8px;background:var(--blue)}
.envelope .band-tip{position:absolute;right:0;bottom:8px;width:200px;height:6px;background:var(--blue);clip-path:polygon(10px 0,100% 0,100% 100%,0 100%)}
</style>
</head>
<body>

<section class="sheet letterhead">
  <div class="wordmark">
    <span class="dot"></span>
    <div><div class="name">Nodeway Summit<br>Private Limited</div><div class="tagline">Powered by innovation</div></div>
  </div>
  <div class="rule-top"></div>
  <div class="rule-under"></div>
  <div class="network" role="img" aria-label="Large faint network of linked nodes in pale blue"></div>
  <div class="contact">
    <span><svg viewBox="0 0 10 10"><rect x="0.5" y="2" width="9" height="6" fill="none" stroke="currentColor"/><path d="M.5 2 5 5.5 9.5 2" fill="none" stroke="currentColor"/></svg>info@nodewaysummit.com</span>
    <span><svg viewBox="0 0 10 10"><path d="M2 1 4 3 3 4.5Q4.5 6.5 5.5 7L7 6 9 8 7.5 9.5Q3 9 .5 2.5Z" fill="currentColor"/></svg>800-555-0142</span>
    <span><svg viewBox="0 0 10 10"><circle cx="5" cy="5" r="4.3" fill="none" stroke="currentColor"/><path d="M.7 5h8.6M5 .7q-3 4.3 0 8.6q3-4.3 0-8.6" fill="none" stroke="currentColor"/></svg>www.nodewaysummit.com</span>
  </div>
  <div class="band"></div>
</section>

<section class="sheet card card-front">
  <div class="network" role="img" aria-label="White network of linked nodes"></div>
  <div class="name-block">
    <div class="name">Nodeway Summit<br>Private Limited</div>
    <div class="tagline">Powered by innovation</div>
  </div>
  <div class="web-band">www.nodewaysummit.com</div>
</section>

<section class="sheet card card-back">
  <div class="wordmark">
    <span class="dot"></span>
    <div><div class="name">Nodeway Summit<br>Private Limited</div><div class="tagline">Powered by innovation</div></div>
  </div>
  <div class="divider"></div>
  <div class="person"><span class="full">Daniel Reyes</span><span class="bar">|</span><span class="role">Chief Operating Officer</span></div>
  <div class="address"><svg viewBox="0 0 10 10"><path d="M5 0a3.5 3.5 0 0 0-3.5 3.5C1.5 6 5 10 5 10s3.5-4 3.5-6.5A3.5 3.5 0 0 0 5 0z" fill="#3176b5"/></svg>12 Harbor Lane, Springfield</div>
  <div class="lines">
    <span><svg viewBox="0 0 10 10"><rect y="2" width="10" height="6" fill="#3176b5"/></svg>info@nodewaysummit.com</span>
    <span><svg viewBox="0 0 10 10"><path d="M2 1 4 3 3 4.5Q4.5 6.5 5.5 7L7 6 9 8 7.5 9.5Q3 9 .5 2.5Z" fill="#3176b5"/></svg>800-555-0142</span>
  </div>
  <div class="grey-band"></div>
</section>

<section class="sheet envelope">
  <div class="top-rule"></div>
  <div class="network" role="img" aria-label="Faint network of linked nodes in soft blue"></div>
  <div class="wordmark">
    <span class="dot"></span>
    <div><div class="name">Nodeway Summit<br>Private Limited</div><div class="tagline">Powered by innovation</div></div>
  </div>
  <div class="window"></div>
  <div class="return">
    <div><span class="sq"></span>12 Harbor Lane, Suite 4</div>
    <div class="gap"><span class="sq"></span>800-555-0142</div>
    <div><span class="sq"></span>info@nodewaysummit.com</div>
    <div><span class="sq"></span>www.nodewaysummit.com</div>
  </div>
  <div class="band-tip"></div>
  <div class="band"></div>
</section>

</body>
</html>
```